ROLL UP CREATION

For a trade show we need three visuals to be seen see pdf file with slogans and photos. I expect from you a nice and attractive formatting that is urgent. the files must be in high definition for the printer. You will find enclosed the 3 visuals, photos the basic logo by adding the .com and the photo of the Rollup For a trade show we need to see the pdf file with slogans and photos. I expect from you a nice and attractive formatting that is urgent. the files must be in high definition for the printer. For a trade show we need to see the pdf file with slogans and photos. I expect from you a nice and attractive formatting that is urgent. the files must be in high definition for the printer. For a trade show we need to see the pdf file with slogans and photos. I expect from you a nice and attractive formatting that is urgent. the files must be in high definition for the printer. For a trade show we need to see the pdf file with slogans and photos. I expect from you a nice and attractive formatting that is urgent. the files must be in high definition for the printer. For a trade show we need to see the pdf file with slogans and photos. I expect from you a nice and attractive formatting that is urgent. the files must be in high definition for the printer. For a trade show we need to see the pdf file with slogans and photos. I expect from you a nice and attractive formatting that is urgent. the files must be in high definition for the printer. For a trade show we need to see the pdf file with slogans and photos. I expect from you a nice and attractive formatting that is urgent. the files must be in high definition for the printer. For a trade show we need to see the pdf file with slogans and photos. I expect from you a nice and attractive formatting that is urgent. the files must be in high definition for the printer. For a trade show we need to see the pdf file with slogans and photos. I expect from you a nice and attractive formatting that is urgent. the files must be in high definition for the printer.

Target Market(s)

Professional

Industry/Entity Type

Trade

Requirements
Must have
• the project the messages and the photos are chosen all the way to a nice and professional result. This is urgently the size of the rollup is 200/85.
Nice to have
• the bottom of the rollup on 40 cm must be just color because in an exhibition the visitors can not see the messages near the ground.
Should not have
• no green color

```html
<!DOCTYPE html>
<html lang="fr">
<head>
<meta charset="utf-8">
<title>Nestora – roll-ups salon</title>
<link rel="stylesheet" href="https://fonts.googleapis.com/css2?family=Open+Sans:wght@400;600;700;800&display=swap">
<style>
  :root{
    --bg:#eceaea;
    --plum:#a24c94;
    --violet:#7f56ad;
    --blue:#4f63b9;
    --blue-bright:#3d6cd0;
    --white:#ffffff;
  }
  *{box-sizing:border-box;margin:0;padding:0}
  html,body{width:1200px;height:1200px;overflow:hidden;background:var(--bg)}
  body{font-family:"Open Sans",Arial,sans-serif;color:var(--white)}
  .stand-row{position:absolute;inset:0;display:flex;justify-content:center;align-items:center;gap:45px}
  .rollup{position:relative;width:340px;height:800px;overflow:hidden;box-shadow:0 10px 30px rgba(0,0,0,.15)}
  .rollup svg.art{position:absolute;inset:0;width:100%;height:100%}
  .brand{position:absolute;left:0;right:0;display:flex;justify-content:center;align-items:center;gap:14px}
  .brand-dot{width:34px;height:34px;border-radius:50%;background:var(--white)}
  .brand-name{font-size:50px;font-weight:400;letter-spacing:-1px;line-height:1;color:var(--white)}
  .line{position:absolute;left:0;right:0;text-align:center;font-size:19px;font-weight:400;line-height:36px}
  .line b{font-weight:800}
  .line.right{text-align:right;right:14px;left:auto;width:320px;line-height:36px}
</style>
</head>
<body>
<main class="stand-row">

  <!-- Roll-up 1 -->
  <section class="rollup rollup-stress">
    <svg class="art" viewBox="0 0 340 800" preserveAspectRatio="none">
      <defs>
        <linearGradient id="bg1" x1="0" y1="0" x2="0" y2="1">
          <stop offset="0" stop-color="#a24c94"/><stop offset=".55" stop-color="#7f56ad"/><stop offset="1" stop-color="#4f63b9"/>
        </linearGradient>
        <linearGradient id="photo1" x1="0" y1="0" x2="1" y2="1">
          <stop offset="0" stop-color="#7fd3df"/><stop offset=".45" stop-color="#f2f0ee"/><stop offset="1" stop-color="#d9dadd"/>
        </linearGradient>
      </defs>
      <rect width="340" height="800" fill="url(#bg1)"/>
      <path d="M0,200 Q170,300 340,190 L340,560 Q170,620 0,540 Z" fill="#3d6cd0"/>
      <path role="img" aria-label="Photo : femme stressée derrière des dossiers et une calculatrice" d="M0,228 Q170,312 340,225 L340,470 Q170,555 0,465 Z" fill="url(#photo1)"/>
    </svg>
    <div class="brand" style="top:45px"><span class="brand-dot"></span><span class="brand-name">nestora</span></div>
    <p class="line" style="top:136px">Finis le stress pour la gestion</p>
    <p class="line" style="top:172px">de vos copropriétés...</p>
    <p class="line" style="top:600px"><b>NESTORA</b> le portail dédié aux</p>
    <p class="line" style="top:636px">professionnels de l’immobilier</p>
  </section>

  <!-- Roll-up 2 -->
  <section class="rollup rollup-avenir">
    <svg class="art" viewBox="0 0 340 800" preserveAspectRatio="none">
      <defs>
        <linearGradient id="bg2" x1="0" y1="0" x2="0" y2="1">
          <stop offset="0" stop-color="#a24c94"/><stop offset="1" stop-color="#8a52a6"/>
        </linearGradient>
        <radialGradient id="photo2" cx=".45" cy=".75" r=".7">
          <stop offset="0" stop-color="#fff8ec"/><stop offset=".25" stop-color="#d9a36a"/><stop offset=".6" stop-color="#5a3a22"/><stop offset="1" stop-color="#2a1c12"/>
        </radialGradient>
        <linearGradient id="tri2" x1="0" y1="0" x2="1" y2="1">
          <stop offset="0" stop-color="#3d6cd0"/><stop offset=".6" stop-color="#6a5bb3"/><stop offset="1" stop-color="#a24c94"/>
        </linearGradient>
      </defs>
      <rect width="340" height="800" fill="url(#bg2)"/>
      <rect role="img" aria-label="Photo : voyante penchée sur une boule de cristal lumineuse" x="0" y="168" width="340" height="440" fill="url(#photo2)"/>
      <polygon points="0,610 340,480 340,800 0,800" fill="url(#tri2)"/>
      <polygon points="0,700 340,800 0,800" fill="#4f63b9"/>
      <line x1="0" y1="700" x2="340" y2="800" stroke="#2c3f8a" stroke-width="1.5"/>
    </svg>
    <div class="brand" style="top:28px"><span class="brand-dot"></span><span class="brand-name">nestora</span></div>
    <p class="line" style="top:96px">Nous ne pourrons pas</p>
    <p class="line" style="top:132px">prédire votre avenir...</p>
    <p class="line right" style="top:590px">mais avec <b>le DTG</b>, celui</p>
    <p class="line right" style="top:626px">de votre immeuble pour</p>
    <p class="line right" style="top:662px">les <b>10 prochaines</b></p>
    <p class="line right" style="top:698px">années !!</p>
  </section>

  <!-- Roll-up 3 -->
  <section class="rollup rollup-dtg">
    <svg class="art" viewBox="0 0 340 800" preserveAspectRatio="none">
      <defs>
        <linearGradient id="bg3" x1="0" y1="0" x2="0" y2="1">
          <stop offset="0" stop-color="#a24c94"/><stop offset=".4" stop-color="#7f56ad"/><stop offset=".72" stop-color="#a24c94"/><stop offset="1" stop-color="#5a60b8"/>
        </linearGradient>
        <linearGradient id="photo3" x1="0" y1="0" x2="1" y2="1">
          <stop offset="0" stop-color="#e8eaee"/><stop offset=".5" stop-color="#b9c8dc"/><stop offset="1" stop-color="#d6d4d0"/>
        </linearGradient>
      </defs>
      <rect width="340" height="800" fill="url(#bg3)"/>
      <path d="M0,268 Q170,230 340,268 L340,548 Q170,590 0,560 Z" fill="#3d6cd0"/>
      <path role="img" aria-label="Photo : deux hommes étonnés penchés sur un bureau" d="M0,292 Q170,262 340,292 L340,525 Q170,560 0,528 Z" fill="url(#photo3)"/>
    </svg>
    <div class="brand" style="top:60px"><span class="brand-dot"></span><span class="brand-name">nestora</span></div>
    <p class="line" style="top:152px;font-size:18px">La réalisation d’un <b>DTG</b> va étonner</p>
    <p class="line" style="top:186px;font-size:18px">plus d’un copropriétaire !!</p>
    <p class="line" style="top:612px;font-size:18px"><b>Le DTG</b>, l’outil qui optimise vos</p>
    <p class="line" style="top:646px;font-size:18px">charges et votre patrimoine...</p>
  </section>

</main>
</body>
</html>
```